Miss Starlit Sovereign 2024 Female Impersonation Pageant

We need a flyer for our pageant this summer. The theme of the pageant is "Velvet Reverie". Take examples from Barnaby Fizzwick or Percy and the Peppermint Tower. Below is what needs to be included in the flyer

Miss Starlit Sovereign 2024
Velvet Reverie
Date: Sunday, June 30, 2024- 5pm
Location: Larkstone Hall for Performance
Honoring: Opaline Trask, Miss Starlit Sovereign 2023
Featuring: Rorita Vane Sutton, Miss Lumen Regalia 2024

The 3 photos below must be used in the flyer. The photo labeled "logo" should be added somewhere in the flyer.
The photos labeled "RVS2024" and "OT2023" also need to be in the flyer.

Target Market(s)

LGBTQ audience

Industry/Entity Type

Pageantry

Font styles to use
Decorative

Requirements
Must have
• Text listed in project description and photos that were included

```html
<!DOCTYPE html>
<html lang="en">
<head>
<meta charset="utf-8">
<title>Velvet Reverie — Miss Starlit Sovereign 2024</title>
<link rel="stylesheet" href="https://fonts.googleapis.com/css2?family=Great+Vibes&family=Oswald:wght@600&family=Playfair+Display:wght@900&family=Poppins:wght@300;400;600;700&display=swap">
<style>
  :root {
    --page-bg: #e8e8ea;
    --night: #1f0627;
    --plum: #3a1340;
    --nebula: #7a2a3c;
    --ember: #b8463a;
    --ink-white: #ffffff;
    --gold-light: #f6e27a;
    --gold-mid: #d4b13a;
    --gold-deep: #9c7a16;
    --label-yellow: #f3e05a;
    --pill-purple: #5b1470;
    --gown-red: #c8151e;
    --drape-red: #a8101a;
    --velvet-purple: #4a1670;
  }
  * { margin: 0; padding: 0; box-sizing: border-box; }
  html, body { width: 1200px; height: 1200px; overflow: hidden; background: var(--page-bg); }
  .flyer {
    position: absolute; left: 180px; top: 57px; width: 839px; height: 1086px; overflow: hidden;
    font-family: "Poppins", sans-serif; color: var(--ink-white);
    box-shadow: 0 6px 24px rgba(0,0,0,.25);
  }
  .backdrop {
    position: absolute; inset: 0;
    background:
      radial-gradient(ellipse 60% 28% at 45% 52%, rgba(184,70,58,.55), transparent 70%),
      radial-gradient(ellipse 70% 40% at 30% 42%, rgba(122,42,60,.5), transparent 70%),
      linear-gradient(180deg, var(--night) 0%, var(--plum) 35%, #2c0f33 70%, #07030a 100%);
  }
  .drape {
    position: absolute; left: 690px; top: 700px; width: 149px; height: 386px;
    background: linear-gradient(200deg, #d2202a, var(--drape-red) 60%, #5e0810);
    border-top-left-radius: 149px 110px;
  }
  .portrait { position: absolute; }
  .portrait-honoree {
    left: 362px; top: 500px; width: 176px; height: 586px;
    background: linear-gradient(180deg, rgba(230,190,110,.9) 0%, #e0b38a 24%, var(--gown-red) 44%, #8e0d14 100%);
    border-radius: 50% 50% 0 0 / 16% 16% 0 0;
  }
  .portrait-featured {
    left: 545px; top: 722px; width: 278px; height: 364px;
    background: linear-gradient(180deg, #b8894f 0%, #6a4830 30%, var(--velvet-purple) 58%, #2c0c45 100%);
    border-radius: 45% 45% 0 0 / 25% 25% 0 0;
  }
  .brand-mark {
    position: absolute; left: 0; width: 100%; top: 106px;
    display: flex; justify-content: center; align-items: center; gap: 10px;
    font-weight: 600; font-size: 22px;
  }
  .brand-mark .dot { width: 14px; height: 14px; border-radius: 50%; background: var(--gold-mid); }
  .presenter {
    position: absolute; left: 0; width: 100%; top: 216px; text-align: center;
    font-weight: 600; font-size: 27px; line-height: 1.2; letter-spacing: .3px;
  }
  .presenter .year { font-weight: 400; }
  .presents {
    position: absolute; left: 0; width: 100%; top: 256px;
    display: flex; justify-content: center; align-items: center; gap: 8px;
    font-size: 16px; line-height: 1; letter-spacing: 6px;
  }
  .presents .rule { width: 98px; height: 1px; background: var(--gold-mid); }
  .theme-script {
    position: absolute; left: 0; width: 100%; top: 286px; text-align: center;
    font-family: "Great Vibes", cursive; font-size: 100px; line-height: 1;
  }
  .theme-main {
    position: absolute; left: 0; width: 100%; top: 370px; text-align: center;
    font-family: "Playfair Display", serif; font-weight: 900; font-size: 74px; line-height: 1; letter-spacing: 1px;
    background: linear-gradient(180deg, var(--gold-light), var(--gold-mid) 55%, var(--gold-deep));
    -webkit-background-clip: text; background-clip: text; color: transparent;
  }
  .date-day {
    position: absolute; left: 60px; top: 470px;
    font-family: "Oswald", sans-serif; font-weight: 600; font-size: 132px; line-height: 1; letter-spacing: -3px;
    background: linear-gradient(180deg, var(--gold-light), var(--gold-mid) 60%, var(--gold-deep));
    -webkit-background-clip: text; background-clip: text; color: transparent;
  }
  .date-month { position: absolute; left: 184px; top: 478px; font-weight: 600; font-size: 58px; line-height: 1; }
  .date-year { position: absolute; left: 184px; top: 534px; font-weight: 400; font-size: 58px; line-height: 1; }
  .time-pill {
    position: absolute; left: 68px; top: 602px; width: 273px; height: 54px;
    display: flex; border-radius: 27px; overflow: hidden;
  }
  .time-pill .weekday { width: 181px; background: var(--pill-purple); display: flex; align-items: center; justify-content: center; font-size: 30px; }
  .time-pill .hour {
    flex: 1; background: linear-gradient(90deg, var(--gold-deep), var(--gold-light) 50%, var(--gold-mid));
    color: #111; font-weight: 700; font-size: 25px; display: flex; align-items: center; justify-content: center;
  }
  .venue { position: absolute; left: 72px; top: 673px; display: flex; gap: 11px; }
  .venue svg { margin-top: 4px; }
  .venue-text { font-size: 22px; line-height: 1.35; }
  .venue-text strong { font-weight: 600; }
  .billing { position: absolute; left: 545px; }
  .billing-honoring { top: 470px; }
  .billing-featuring { top: 594px; }
  .billing .label { color: var(--label-yellow); font-weight: 700; font-size: 18px; letter-spacing: 2px; line-height: 1.35; }
  .billing .name { font-weight: 600; font-size: 21px; line-height: 1.35; }
  .billing .title-sub { font-weight: 300; font-size: 18px; letter-spacing: 2px; line-height: 1.3; }
  .hosts { position: absolute; left: 60px; top: 908px; }
  .hosts .label { color: var(--label-yellow); font-weight: 700; font-size: 21px; letter-spacing: 4px; line-height: 1.2; }
  .hosts .names { margin-top: 14px; font-weight: 600; font-size: 24px; letter-spacing: 2.5px; line-height: 1.25; }
</style>
</head>
<body>
  <main class="flyer">
    <div class="backdrop" role="img" aria-label="Starry purple and red nebula sky over a dusky mountain horizon"></div>
    <div class="drape" role="img" aria-label="Red velvet stage curtain"></div>
    <div class="portrait portrait-honoree" role="img" aria-label="Photo of Opaline Trask in a red sequined gown and crown"></div>
    <div class="portrait portrait-featured" role="img" aria-label="Photo of Rorita Vane Sutton in a purple velvet coat and tall top hat, holding a crown"></div>

    <div class="brand-mark"><span class="dot"></span>Miss Starlit Sovereign</div>

    <h1 class="presenter">MISS STARLIT SOVEREIGN <span class="year">2024</span></h1>
    <div class="presents"><span class="rule"></span>PRESENTS<span class="rule"></span></div>
    <div class="theme-script">Velvet</div>
    <div class="theme-main">REVERIE</div>

    <div class="date-day">30</div>
    <div class="date-month">JUNE</div>
    <div class="date-year">2024</div>
    <div class="time-pill"><span class="weekday">SUNDAY</span><span class="hour">5PM</span></div>

    <div class="venue">
      <svg width="31" height="43" viewBox="0 0 34 46" aria-hidden="true">
        <path d="M17 2C8.7 2 2 8.7 2 17c0 11 15 27 15 27s15-16 15-27C32 8.7 25.3 2 17 2z" fill="var(--gold-mid)"/>
        <circle cx="17" cy="17" r="6" fill="var(--plum)"/>
      </svg>
      <div class="venue-text"><strong>Larkstone Hall</strong><br>for <strong>Performance</strong></div>
    </div>

    <section class="billing billing-honoring">
      <div class="label">Honoring</div>
      <div class="name">OPALINE TRASK</div>
      <div class="name">MISS STARLIT</div>
      <div class="title-sub">Sovereign 2023</div>
    </section>
    <section class="billing billing-featuring">
      <div class="label">Featuring</div>
      <div class="name">RORITA VANE SUTTON</div>
      <div class="name">MISS LUMEN</div>
      <div class="title-sub">Regalia 2024</div>
    </section>

    <section class="hosts">
      <div class="label">Hosted by</div>
      <div class="names">JUNO CASTELLANE<br>&amp; CELESTINE</div>
    </section>
  </main>
</body>
</html>
```